Hello,

I need a logo design for a card game we are developing for our friends. Our idea is to create a drinking and party game for our friend group. The game actually is completely finished only thing missing is the design of the cards text and the logo on the back.

Back-card logo should state "Midnight Pebble Riddles" in a cool print, and it should be eye-catching. Literally, we just want to see cool ideas and see what we like.

The front of the cards should be designed in a way that text inside them can be modified in an example "Photoshop".

The front card will only include text. Text should read in the cards in two ways up and down so it will be easy to read from both sides of the table.

You can use the sample text: "The one time I designed a card..."

```html
<!DOCTYPE html>
<html lang="en">
<head>
<meta charset="utf-8">
<title>Midnight Pebble Riddles – Card Back and Front</title>
<link href="https://fonts.googleapis.com/css2?family=Urbanist:wght@700&display=swap" rel="stylesheet">
<style>
  :root {
    --card-red: #c4202f;
    --card-red-deep: #b31c2a;
    --paper: #ffffff;
    --canvas: #fefefe;
    --shadow: rgba(0, 0, 0, 0.45);
  }
  * { margin: 0; padding: 0; box-sizing: border-box; }
  html, body {
    width: 1200px;
    height: 1200px;
    overflow: hidden;
    background: var(--canvas);
  }
  .stage {
    position: relative;
    width: 1200px;
    height: 1200px;
    font-family: "Urbanist", "Century Gothic", sans-serif;
  }
  .card {
    position: absolute;
    top: 332px;
    width: 354px;
    height: 552px;
    border-radius: 26px;
    background: var(--paper);
    box-shadow: 6px 7px 8px var(--shadow);
  }
  .card--back { left: 190px; }
  .card--front { left: 656px; }

  .card-back__field {
    position: absolute;
    inset: 9px;
    border-radius: 20px;
    background: linear-gradient(135deg, var(--card-red) 0%, var(--card-red-deep) 100%);
  }
  .card-back__badge {
    position: absolute;
    left: 54px;
    top: 194px;
    width: 246px;
    height: 156px;
    border-radius: 78px / 78px;
    background: var(--paper);
    display: flex;
    flex-direction: column;
    align-items: center;
    justify-content: center;
    text-align: center;
  }
  .card-back__title {
    color: var(--card-red);
    font-weight: 700;
    font-size: 30px;
    line-height: 1.02;
    letter-spacing: -0.5px;
  }

  .card-front__prompt {
    position: absolute;
    left: 0;
    width: 100%;
    text-align: center;
    color: var(--card-red);
    font-weight: 700;
    font-size: 17px;
    letter-spacing: 0.2px;
  }
  .card-front__prompt--top {
    top: 122px;
    transform: rotate(180deg);
  }
  .card-front__prompt--bottom { top: 396px; }
  .card-front__divider {
    position: absolute;
    left: 18px;
    right: 18px;
    top: 275px;
    height: 2px;
    background: var(--card-red);
  }
</style>
</head>
<body>
  <main class="stage">
    <section class="card card--back" aria-label="Card back">
      <div class="card-back__field" role="img" aria-label="Red background with fine diagonal cross-hatch pattern"></div>
      <div class="card-back__badge">
        <h1 class="card-back__title">Midnight<br>Pebble<br>Riddles</h1>
      </div>
    </section>

    <section class="card card--front" aria-label="Card front">
      <p class="card-front__prompt card-front__prompt--top">The one time I designed a card...</p>
      <div class="card-front__divider"></div>
      <p class="card-front__prompt card-front__prompt--bottom">The one time I designed a card...</p>
    </section>
  </main>
</body>
</html>
```